Equity, Effectiveness and Efficiency in charitable food relief sector

I am undertaking my PhD in food policy in the charitable food relief sector, specifically investigating the factors (supply, demand and capacity) that affect the introduction of nutrition policy and in turn, affect the sector's ability to achieve equity, effectiveness and efficiency.

I need a graphic device that incorporates this central idea of Equity, Effectiveness and Efficiency, and how the factors of supply, demand and capacity interact. There are sub-factors within supply (1-6), demand (7-10) and capacity (11 - 15). All these details are shown in the attached figure (Basic figure_Eq Effec Effic and factors.jpg)

This figure (Basic figure_Eq Effec Effic and factors.jpg) contains all the information I need in a graphic but I need something that is more visually appealing, and that can link the ideas in a format other than a table. The final graphic will outline how the food relief sector balances the core objectives of equity, effectiveness and efficiency with the factors (and sub-factors) of supply, demand and capacity.

```html
<!DOCTYPE html>
<html lang="en">
<head>
<meta charset="utf-8">
<title>Factors Affecting The Introduction Of Nutrition Policy</title>
<link href="https://fonts.googleapis.com/css2?family=Poppins:wght@400;500;600;700;800&display=swap" rel="stylesheet">
<style>
  :root{
    --supply:#1b75bb;
    --supply-dark:#135f9c;
    --capacity:#3f9b35;
    --capacity-dark:#2f7f28;
    --demand:#e0223d;
    --demand-dark:#c21a33;
    --demand-ring:#5fae4b;
    --demand-ring-dark:#3f8f35;
    --cap-ring:#f29a2e;
    --cap-ring-dark:#d97c12;
    --ink:#111111;
    --muted:#3a3a3a;
    --track:#c9cacc;
    --map:#eef0f2;
    --paper:#ffffff;
  }
  html,body{margin:0;padding:0;overflow:hidden;background:var(--paper);}
  .canvas{width:946px;height:1200px;display:block;font-family:'Poppins',sans-serif;}
  .title{font-weight:800;font-size:15px;fill:var(--ink);text-anchor:middle;}
  .factor-label{font-size:8px;fill:var(--muted);}
  .factor-label.end{text-anchor:end;}
  .factor-label.mid{text-anchor:middle;}
  .sub-label{font-size:7.5px;fill:var(--muted);}
  .badge-num{font-size:9px;font-weight:700;fill:#fff;text-anchor:middle;dominant-baseline:central;}
  .venn-label{font-size:11px;font-weight:700;fill:#fff;text-anchor:middle;}
  .core-label{font-size:10px;font-weight:700;fill:#2b2b2b;text-anchor:middle;}
  .ring-title{font-size:14px;font-weight:700;fill:var(--ink);text-anchor:middle;}
  .seg-label{font-size:7.5px;fill:#fff;text-anchor:middle;}
  .band-label{font-size:8px;fill:#fff;text-anchor:middle;}
  .arc-text{font-size:10.5px;font-weight:700;fill:#3b3b3b;letter-spacing:.2px;}
  .bullet-line{stroke:#555;stroke-width:.8;fill:none;}
</style>
</head>
<body>
<svg class="canvas" viewBox="0 0 850 1080" preserveAspectRatio="none" xmlns="http://www.w3.org/2000/svg">
  <defs>
    <radialGradient id="coreGlow" cx="50%" cy="45%" r="60%">
      <stop offset="0%" stop-color="#ffffff"/>
      <stop offset="80%" stop-color="#f6f6f6"/>
      <stop offset="100%" stop-color="#e6e6e6"/>
    </radialGradient>
    <linearGradient id="bandFlow" x1="0" y1="0" x2="1" y2="0">
      <stop offset="0%" stop-color="#1e73b8"/>
      <stop offset="25%" stop-color="#1e73b8"/>
      <stop offset="50%" stop-color="#4fa35a"/>
      <stop offset="72%" stop-color="#b2a532"/>
      <stop offset="100%" stop-color="#f26a22"/>
    </linearGradient>
    <path id="arcDemand" d="M314,629 A108 108 0 0 1 466,489.5"/>
    <path id="arcSupply" d="M145,713 A112 112 0 0 0 243,854"/>
    <path id="arcCapacity" d="M472,713 A112 112 0 0 0 570,854"/>
  </defs>

  <!-- ============ Top: circular factor wheel ============ -->
  <text class="title" x="418" y="44">Factors Affecting The Introducton Of Nutrition Policy</text>

  <rect x="190" y="80" width="520" height="360" rx="40" fill="var(--map)" role="img" aria-label="Faint world map backdrop"/>

  <circle cx="411" cy="262" r="164" fill="none" stroke="var(--track)" stroke-width="4"/>

  <g class="venn">
    <circle cx="372" cy="236" r="86" fill="var(--supply)" opacity=".95"/>
    <circle cx="458" cy="236" r="86" fill="var(--capacity)" opacity=".9"/>
    <circle cx="414" cy="314" r="84" fill="var(--demand)" opacity=".88"/>
    <circle cx="413" cy="256" r="54" fill="url(#coreGlow)"/>
    <text class="venn-label" transform="translate(336,212) rotate(-72)">Supply</text>
    <text class="venn-label" transform="translate(490,208) rotate(72)">Capacity</text>
    <text class="venn-label" x="414" y="340">Demand</text>
    <text class="core-label" x="413" y="242">Equity,</text>
    <text class="core-label" x="413" y="256">Effectiveness,</text>
    <text class="core-label" x="413" y="270">Efficiency</text>
  </g>

  <g class="badges">
    <g fill="var(--supply)" stroke="#fff" stroke-width="2">
      <circle cx="410" cy="98" r="9"/><circle cx="350" cy="112" r="9"/><circle cx="299" cy="148" r="9"/>
      <circle cx="268" cy="202" r="9"/><circle cx="260" cy="266" r="9"/><circle cx="283" cy="325" r="9"/>
    </g>
    <g fill="var(--demand)" stroke="#fff" stroke-width="2">
      <circle cx="323" cy="372" r="9"/><circle cx="381" cy="397" r="9"/><circle cx="443" cy="397" r="9"/><circle cx="501" cy="372" r="9"/>
    </g>
    <g fill="var(--capacity)" stroke="#fff" stroke-width="2">
      <circle cx="543" cy="325" r="9"/><circle cx="563" cy="265" r="9"/><circle cx="556" cy="202" r="9"/>
      <circle cx="523" cy="148" r="9"/><circle cx="473" cy="112" r="9"/>
    </g>
    <text class="badge-num" x="410" y="98">1</text><text class="badge-num" x="350" y="112">2</text>
    <text class="badge-num" x="299" y="148">3</text><text class="badge-num" x="268" y="202">4</text>
    <text class="badge-num" x="260" y="266">5</text><text class="badge-num" x="283" y="325">6</text>
    <text class="badge-num" x="323" y="372">7</text><text class="badge-num" x="381" y="397">8</text>
    <text class="badge-num" x="443" y="397">9</text><text class="badge-num" x="501" y="372">10</text>
    <text class="badge-num" x="543" y="325">11</text><text class="badge-num" x="563" y="265">12</text>
    <text class="badge-num" x="556" y="202">13</text><text class="badge-num" x="523" y="148">14</text>
    <text class="badge-num" x="473" y="112">15</text>
  </g>

  <g class="wheel-labels">
    <text class="factor-label mid" x="410" y="72">Uncertain</text>
    <text class="factor-label mid" x="410" y="82">material supply</text>
    <text class="factor-label mid" x="302" y="93">Uncertain</text>
    <text class="factor-label mid" x="302" y="103">monetary supply</text>
    <text class="factor-label end" x="284" y="140">Limited</text>
    <text class="factor-label end" x="284" y="150">food supply</text>
    <text class="factor-label end" x="252" y="205">Perishability</text>
    <text class="factor-label end" x="244" y="262">Donor</text>
    <text class="factor-label end" x="244" y="272">constraints</text>
    <text class="factor-label end" x="262" y="323">Donor</text>
    <text class="factor-label end" x="262" y="333">relationships</text>
    <text class="factor-label mid" x="293" y="393">Uncertain</text>
    <text class="factor-label mid" x="293" y="403">demand</text>
    <text class="factor-label mid" x="380" y="423">Limited</text>
    <text class="factor-label mid" x="380" y="433">demand visibility</text>
    <text class="factor-label mid" x="447" y="423">Client</text>
    <text class="factor-label mid" x="447" y="433">choice</text>
    <text class="factor-label" x="512" y="392">Food</text>
    <text class="factor-label" x="512" y="402">wastage</text>
    <text class="factor-label" x="566" y="329">Storage</text>
    <text class="factor-label" x="581" y="269">Transportation</text>
    <text class="factor-label" x="574" y="205">Workforce</text>
    <text class="factor-label" x="541" y="141">External</text>
    <text class="factor-label" x="541" y="151">stakeholders</text>
    <text class="factor-label" x="489" y="96">Budget</text>

    <path class="bullet-line" d="M603,326 H630 M630,320 V332 H642 M630,320 H642"/>
    <g fill="var(--capacity)"><circle cx="644" cy="320" r="2"/><circle cx="644" cy="332" r="2"/></g>
    <text class="sub-label" x="651" y="323">Cold</text>
    <text class="sub-label" x="651" y="335">Warehouse</text>

    <path class="bullet-line" d="M615,202 H630 M630,180 V228 M630,180 H642 M630,192 H642 M630,204 H642 M630,216 H642 M630,228 H642"/>
    <g fill="var(--capacity)">
      <circle cx="644" cy="180" r="2"/><circle cx="644" cy="192" r="2"/><circle cx="644" cy="204" r="2"/>
      <circle cx="644" cy="216" r="2"/><circle cx="644" cy="228" r="2"/>
    </g>
    <text class="sub-label" x="651" y="183">Volunteers</text>
    <text class="sub-label" x="651" y="195">Expertise and training</text>
    <text class="sub-label" x="651" y="207">Attitudes and Beliefs</text>
    <text class="sub-label" x="651" y="219">Collaboration</text>
    <text class="sub-label" x="651" y="231">Executive Support</text>
  </g>

  <!-- ============ Bottom: linked ring diagram ============ -->
  <g class="flow-band">
    <polygon points="63,628 745,628 765,654 745,680 63,680 78,654" fill="url(#bandFlow)"/>
    <text class="band-label" x="158" y="655">Uncertain</text>
    <text class="band-label" x="158" y="665">material supply</text>
    <text class="band-label" x="710" y="658">Budget</text>
    <circle cx="152" cy="628" r="9" fill="var(--supply-dark)" stroke="#fff" stroke-width="2"/>
    <text class="badge-num" x="152" y="628">1</text>
    <circle cx="706" cy="628" r="9" fill="#e05a14" stroke="#fff" stroke-width="2"/>
    <text class="badge-num" x="706" y="628">15</text>
  </g>

  <!-- Demand ring -->
  <g class="ring demand">
    <circle cx="412" cy="583" r="70" fill="none" stroke="var(--demand-ring)" stroke-width="50" opacity=".95"
      pathLength="360" stroke-dasharray="70 5 70 5 70 5 70 65" transform="rotate(160 412 583)"/>
    <circle cx="412" cy="583" r="45" fill="#fff"/>
    <text class="ring-title" x="412" y="588">Demand</text>
    <g fill="var(--demand-ring-dark)" stroke="#fff" stroke-width="2">
      <circle cx="362" cy="570" r="9"/><circle cx="412" cy="531" r="9"/><circle cx="462" cy="570" r="9"/><circle cx="438" cy="628" r="9"/>
    </g>
    <text class="badge-num" x="362" y="570">10</text><text class="badge-num" x="412" y="531">9</text>
    <text class="badge-num" x="462" y="570">8</text><text class="badge-num" x="438" y="628">7</text>
    <text class="seg-label" transform="translate(337,563) rotate(-75)">Food</text>
    <text class="seg-label" transform="translate(345,563) rotate(-75)">wastage</text>
    <text class="seg-label" x="412" y="508">Client</text>
    <text class="seg-label" x="412" y="517">choice</text>
    <text class="seg-label" transform="translate(484,562) rotate(75)">Limited</text>
    <text class="seg-label" transform="translate(476,562) rotate(75)">demand visibility</text>
    <text class="seg-label" transform="translate(455,640) rotate(-60)">Uncertain</text>
    <text class="seg-label" transform="translate(463,645) rotate(-60)">demand</text>
    <text class="arc-text"><textPath href="#arcDemand">Equity, Effectiveness, Efficiency</textPath></text>
  </g>

  <!-- Supply ring -->
  <g class="ring supply">
    <circle cx="253" cy="742" r="70" fill="none" stroke="var(--supply)" stroke-width="50"
      pathLength="360" stroke-dasharray="50 4 50 4 50 4 50 4 50 94" transform="rotate(-70 253 742)"/>
    <circle cx="253" cy="742" r="45" fill="#fff"/>
    <text class="ring-title" x="253" y="747">Supply</text>
    <g fill="var(--supply-dark)" stroke="#fff" stroke-width="2">
      <circle cx="290" cy="705" r="9"/><circle cx="304" cy="750" r="9"/><circle cx="277" cy="788" r="9"/>
      <circle cx="229" cy="788" r="9"/><circle cx="202" cy="750" r="9"/>
    </g>
    <text class="badge-num" x="290" y="705">2</text><text class="badge-num" x="304" y="750">3</text>
    <text class="badge-num" x="277" y="788">4</text><text class="badge-num" x="229" y="788">5</text>
    <text class="badge-num" x="202" y="750">6</text>
    <text class="seg-label" transform="translate(304,682) rotate(40)">Uncertain</text>
    <text class="seg-label" transform="translate(298,690) rotate(40)">monetary supply</text>
    <text class="seg-label" transform="translate(326,745) rotate(99)">Limited</text>
    <text class="seg-label" transform="translate(318,745) rotate(99)">food supply</text>
    <text class="seg-label" transform="translate(292,813) rotate(-30)">Perishability</text>
    <text class="seg-label" transform="translate(210,805) rotate(30)">Donor</text>
    <text class="seg-label" transform="translate(206,813) rotate(30)">constraints</text>
    <text class="seg-label" transform="translate(180,745) rotate(-95)">Donor</text>
    <text class="seg-label" transform="translate(188,745) rotate(-95)">relationships</text>
    <text class="arc-text"><textPath href="#arcSupply">Equity, Effectiveness, Efficiency</textPath></text>
  </g>

  <!-- Capacity ring -->
  <g class="ring capacity">
    <circle cx="580" cy="742" r="70" fill="none" stroke="var(--cap-ring)" stroke-width="50"
      pathLength="360" stroke-dasharray="70 5 70 5 70 5 70 65" transform="rotate(-95 580 742)"/>
    <circle cx="580" cy="742" r="45" fill="#fff"/>
    <text class="ring-title" x="580" y="747">Capacity</text>
    <g fill="var(--cap-ring-dark)" stroke="#fff" stroke-width="2">
      <circle cx="606" cy="697" r="9"/><circle cx="630" cy="755" r="9"/><circle cx="580" cy="794" r="9"/><circle cx="529" cy="751" r="9"/>
    </g>
    <text class="badge-num" x="606" y="697">11</text><text class="badge-num" x="630" y="755">12</text>
    <text class="badge-num" x="580" y="794">13</text><text class="badge-num" x="529" y="751">14</text>
    <g transform="translate(622,668) rotate(35)">
      <text class="seg-label" x="0" y="0">Storage</text>
      <text class="seg-label" x="0" y="9">• Cold</text>
      <text class="seg-label" x="0" y="18">• Warehouse</text>
    </g>
    <text class="seg-label" transform="translate(657,760) rotate(-80)">Transportation</text>
    <text class="seg-label" x="580" y="830">Workforce</text>
    <text class="seg-label" transform="translate(500,745) rotate(75)">External</text>
    <text class="seg-label" transform="translate(508,745) rotate(75)">stakeholders</text>
    <text class="arc-text"><textPath href="#arcCapacity">Equity, Effectiveness, Efficiency</textPath></text>

    <path class="bullet-line" d="M582,848 V906 M582,858 H592 M582,870 H592 M582,882 H592 M582,894 H592 M582,906 H592"/>
    <g fill="var(--cap-ring)">
      <circle cx="594" cy="858" r="2"/><circle cx="594" cy="870" r="2"/><circle cx="594" cy="882" r="2"/>
      <circle cx="594" cy="894" r="2"/><circle cx="594" cy="906" r="2"/>
    </g>
    <text class="sub-label" x="601" y="861">Volunteers</text>
    <text class="sub-label" x="601" y="873">Expertise and training</text>
    <text class="sub-label" x="601" y="885">Attitudes and Beliefs</text>
    <text class="sub-label" x="601" y="897">Collaboration</text>
    <text class="sub-label" x="601" y="909">Executive Support</text>
  </g>

  <text class="title" x="433" y="955">Factors Affecting The Introducton Of Nutrition Policy</text>
</svg>
</body>
</html>
```